Brenmor Water - 500ml

to create a water bottle packaging similar to Brume Claire design. Bottle should be blue similar to NORTH KIND but change the design/logo to Brenmor. Wording should be similar just different design and logo. Thanks.

Colors
0054AA
0677BA
7BADD7
CADEEF
E8F1F8

Requirements
Must have
• Bottle must not be in plastic bottles. They are made in a carton instead - see NORTH KIND for reference.

```html
<!DOCTYPE html>
<html lang="en">
<head>
<meta charset="utf-8">
<title>Brenmor Water – 500 ml carton front panel</title>
<link rel="stylesheet" href="https://fonts.googleapis.com/css2?family=Oswald:wght@300;400&family=Montserrat:wght@500;700&display=swap">
<style>
  :root {
    --blue-deep: #0054AA;
    --blue-mid: #0677BA;
    --blue-soft: #7BADD7;
    --blue-pale: #CADEEF;
    --blue-mist: #E8F1F8;
    --white: #FFFFFF;
  }
  html, body {
    margin: 0;
    padding: 0;
    width: 843px;
    height: 1200px;
    overflow: hidden;
    background: var(--blue-deep);
  }
  .carton-front {
    position: relative;
    width: 843px;
    height: 1200px;
    overflow: hidden;
    background: linear-gradient(180deg, var(--blue-mid) 0%, var(--blue-deep) 55%, #004a98 100%);
    color: var(--white);
    font-family: "Montserrat", Arial, sans-serif;
    text-align: center;
  }
  .mountain-scene {
    position: absolute;
    left: 0;
    top: 70px;
    width: 843px;
    height: 270px;
    background:
      linear-gradient(180deg, rgba(232,241,248,0) 0%, rgba(232,241,248,0.95) 38%, rgba(202,222,239,0.9) 58%, rgba(123,173,215,0.75) 78%, rgba(6,119,186,0) 100%);
  }
  .brand {
    position: absolute;
    left: 0;
    right: 0;
    top: 368px;
  }
  .brand-name {
    margin: 0;
    font-family: "Montserrat", Arial, sans-serif;
    font-weight: 700;
    font-size: 64px;
    line-height: 1;
    letter-spacing: 1px;
    color: var(--white);
  }
  .brand-tagline {
    margin: 10px 0 0;
    font-size: 11px;
    font-weight: 500;
    letter-spacing: 2px;
    color: var(--blue-mist);
  }
  .product-name {
    position: absolute;
    left: 0;
    right: 0;
    top: 500px;
    margin: 0;
    font-family: "Oswald", "Arial Narrow", sans-serif;
    font-weight: 300;
    font-size: 230px;
    line-height: 1;
    letter-spacing: 6px;
    color: var(--white);
  }
  .product-claim {
    position: absolute;
    left: 0;
    right: 0;
    top: 870px;
  }
  .claim-title {
    margin: 0;
    font-weight: 700;
    font-size: 30px;
    color: var(--white);
  }
  .claim-detail {
    margin: 12px 0 0;
    font-weight: 500;
    font-size: 23px;
    line-height: 1.35;
    color: var(--blue-pale);
  }
  .volume {
    position: absolute;
    left: 0;
    right: 0;
    top: 1075px;
    margin: 0;
    font-family: "Oswald", "Arial Narrow", sans-serif;
    font-weight: 400;
    font-size: 38px;
    letter-spacing: 1px;
    color: var(--white);
  }
</style>
</head>
<body>
  <main class="carton-front">
    <div class="mountain-scene" role="img" aria-label="Illustration of snow-capped mountain peaks above a misty lake"></div>

    <div class="brand">
      <p class="brand-name">Brenmor</p>
      <p class="brand-tagline">PURE WATERS SINCE 1998</p>
    </div>

    <h1 class="product-name">WATER</h1>

    <div class="product-claim">
      <p class="claim-title">100% Spring Water</p>
      <p class="claim-detail">Sustainably sourced water<br>in a plant-based carton</p>
    </div>

    <p class="volume">500 ML</p>
  </main>
</body>
</html>
```